Melbourne Locksmith Needs a Web Site

We need a web site for our new Locksmith business in Melbourne Australia. Our business is called " Corbett Row Locksmiths" . (Corbett row is a well known in the city and has the famous railway station , it is a main icon of melbourne . Maybe we could incorperate the station maybe in the front page or heading background. our services include Automotive Locksmithing ( Cuting keys to cars, opening cars etc / Master Keys Systems/ Commercial work / Domestic . Also we have no logo yet. but we can get that in the future if needed.

Target Market(s)

(Automotive ) Lost keys to cars, Trucks, Jammed Ignitions, Opening Vehicles. mobile locksmith in a van, Locked out of your house ?

Industry/Entity Type

Business

Number of Pages Required

4 page

Font styles to use
Sans Serif

Colors

Designer to choose colors to be used in the design.

Requirements
Must have
• Phone number easy to read on web site.
Nice to have
• map of where we are, show case pictures of common lock problems for automotive eg ( damaged keys/ Broken).

```html
<!DOCTYPE html>
<html lang="en">
<head>
<meta charset="utf-8">
<title>Corbett Row Locksmiths</title>
<link href="https://fonts.googleapis.com/css2?family=Roboto:wght@300;400;500&family=Open+Sans:wght@400;600&display=swap" rel="stylesheet">
<style>
:root{
  --blue:#1a84e0;
  --navy:#1b2a86;
  --footer:#1c2463;
  --ink:#222;
  --muted:#6f6f6f;
  --frame:#d6d6d6;
  --panel:#f2f2f2;
  --white:#fff;
}
*{margin:0;padding:0;box-sizing:border-box}
html,body{width:1200px;height:2546px;overflow:hidden;background:var(--white)}
body{position:relative;font-family:'Roboto',sans-serif;color:var(--ink)}
a{color:inherit;text-decoration:none}

/* header */
.site-header{position:absolute;top:0;left:0;width:1200px;height:98px;background:var(--white)}
.brand{position:absolute;left:115px;top:36px;color:var(--navy);font-weight:500;font-size:22px;line-height:26px;letter-spacing:.4px;white-space:nowrap}
.main-nav{position:absolute;left:430px;top:36px;display:flex;gap:27px;font-size:17px;color:#555}
.main-nav .active{color:var(--blue)}
.header-phone{position:absolute;left:928px;top:32px;display:flex;align-items:center;gap:8px;font-size:20px;color:#222}

/* hero */
.hero{position:absolute;top:98px;left:0;width:1200px;height:557px;
  background:linear-gradient(180deg,#4f8fd6 0%,#8dbbe8 30%,#d9a53a 45%,#c98a2a 70%,#6e6a66 100%)}
.hero-caption{position:absolute;left:119px;top:262px;width:455px;height:193px;
  background:rgba(30,42,112,.85);color:var(--white);padding:28px 38px;
  font-weight:300;font-size:38px;line-height:43px;text-transform:uppercase}
.hero-dots{position:absolute;left:556px;top:513px;display:flex;gap:9px}
.hero-dots span{width:14px;height:14px;border-radius:50%;border:2px solid var(--white)}
.hero-dots span.on{background:var(--white)}

/* services */
.service{position:absolute;top:701px;width:210px;height:273px}
.service .arch{position:absolute;left:36px;top:0;width:138px;height:145px;
  border:6px solid var(--frame);border-bottom:none;border-radius:69px 69px 0 0;
  display:flex;align-items:center;justify-content:center;padding-top:18px}
.service .box{position:absolute;left:0;top:139px;width:210px;height:134px;
  border:6px solid var(--frame);text-align:center;padding-top:26px}
.service h3{font-weight:400;font-size:18px;line-height:22px;color:var(--navy);text-transform:uppercase}
.service .more{display:inline-block;margin-top:10px;font-size:14px;color:var(--blue)}
.s1{left:143px}.s2{left:382px}.s3{left:623px}.s4{left:862px}

/* why */
.why{position:absolute;top:1057px;left:0;width:1200px;height:430px;background:var(--blue);color:var(--white);text-align:center}
.why .notch{position:absolute;left:562px;top:0}
.why h2{position:absolute;top:82px;width:100%;font-weight:400;font-size:35px}
.why .copy{position:absolute;left:175px;top:141px;width:850px;font-family:'Open Sans',sans-serif;font-size:15px;line-height:25px;color:#dbeafb}
.why .copy p+p{margin-top:14px}
.btn-outline{position:absolute;left:516px;top:319px;width:175px;height:43px;border:2px solid var(--white);
  font-family:'Open Sans',sans-serif;font-weight:600;font-size:15px;line-height:39px;letter-spacing:.5px}

/* cases */
.cases-title{position:absolute;left:124px;top:1524px;font-weight:400;font-size:30px}
.case{position:absolute;top:1578px;width:238px;height:253px}
.case .photo{width:100%;height:100%}
.case .label{position:absolute;left:0;bottom:0;width:100%;height:46px;background:rgba(40,40,40,.75);
  color:var(--white);font-size:19px;line-height:46px;text-align:center}
.c1{left:124px}.c1 .photo{background:linear-gradient(135deg,#e6e6e6,#9c9c9c)}
.c2{left:365px}.c2 .photo{background:linear-gradient(135deg,#d0d0d0,#3a3a3a)}
.c3{left:606px}.c3 .photo{background:linear-gradient(135deg,#ececec,#b4a296)}
.c4{left:847px;width:236px}.c4 .photo{background:linear-gradient(135deg,#d0202a,#6e1a1a)}

/* location */
.location{position:absolute;top:1899px;left:0;width:1200px;height:429px;background:var(--panel)}
.location .eyebrow{position:absolute;left:127px;top:94px;font-size:24px;color:var(--blue)}
.location h2{position:absolute;left:127px;top:128px;font-weight:400;font-size:32px;color:#111}
.location p{position:absolute;left:127px;top:187px;width:290px;font-family:'Open Sans',sans-serif;font-size:15px;line-height:25px;color:var(--muted)}
.location .map{position:absolute;left:448px;top:0;width:752px;height:429px;
  background:linear-gradient(160deg,#efeadf 0%,#e7e2d6 60%,#cfe0c0 85%,#a9cdea 100%)}

/* footer */
.site-footer{position:absolute;top:2328px;left:0;width:1200px;height:218px;background:var(--footer);color:var(--white)}
.contact-item{position:absolute;top:52px;display:flex;align-items:center;gap:9px;font-size:17px}
.ci-addr{left:128px}.ci-phone{left:602px}.ci-mail{left:862px}
.footer-nav{position:absolute;left:129px;top:119px;display:flex;gap:35px;font-size:17px}
.copyright{position:absolute;left:129px;top:154px;font-size:12px;color:#8c93c0}
.social{position:absolute;left:938px;top:114px;display:flex;gap:3px}
.social span{width:32px;height:32px;border-radius:50%;border:2px solid var(--white)}
</style>
</head>
<body>

<header class="site-header">
  <a class="brand" href="#">CORBETT ROW LOCKSMITHS</a>
  <nav class="main-nav">
    <a class="active" href="#">Home</a><a href="#">About Us</a><a href="#">Services</a><a href="#">Cases</a><a href="#">Review</a><a href="#">Contact</a>
  </nav>
  <div class="header-phone">
    <svg width="20" height="20" viewBox="0 0 24 24"><path fill="#1a84e0" d="M6.6 10.8c1.4 2.8 3.8 5.1 6.6 6.6l2.2-2.2c.3-.3.7-.4 1-.2 1.1.4 2.3.6 3.6.6.6 0 1 .4 1 1V20c0 .6-.4 1-1 1C10.6 21 3 13.4 3 4c0-.6.4-1 1-1h3.5c.6 0 1 .4 1 1 0 1.3.2 2.5.6 3.6.1.3 0 .7-.2 1L6.6 10.8z"/></svg>
    <span>(03) 9412 7730</span>
  </div>
</header>

<section class="hero" role="img" aria-label="Photograph of the historic yellow railway station building on Corbett Row under a blue sky">
  <h1 class="hero-caption">Jammed ignitions /<br>locked out of<br>your house ?</h1>
  <div class="hero-dots"><span class="on"></span><span class="on"></span><span class="on"></span><span class="on"></span></div>
</section>

<section class="services">
  <div class="service s1">
    <div class="arch">
      <svg width="62" height="62" viewBox="0 0 64 64" fill="none" stroke="#1a84e0" stroke-width="3.5" stroke-linecap="round" stroke-linejoin="round"><circle cx="20" cy="44" r="13"/><circle cx="20" cy="44" r="5"/><path d="M29 35 56 8M47 17l6 6M41 23l5 5M52 12l4 4"/></svg>
    </div>
    <div class="box"><h3>Cutting key<br>to car</h3><a class="more" href="#">Learn More ›</a></div>
  </div>
  <div class="service s2">
    <div class="arch">
      <svg width="66" height="60" viewBox="0 0 66 60" fill="none" stroke="#1a84e0" stroke-width="3.5" stroke-linejoin="round"><path d="M12 26 18 10c1-3 3-4 6-4h18c3 0 5 1 6 4l6 16"/><rect x="6" y="26" width="54" height="20" rx="5"/><path d="M12 46v8h9v-8M45 46v8h9v-8"/><circle cx="16" cy="36" r="3"/><circle cx="50" cy="36" r="3"/><path d="M26 38h14"/></svg>
    </div>
    <div class="box"><h3>Opening<br>cars</h3><a class="more" href="#">Learn More ›</a></div>
  </div>
  <div class="service s3">
    <div class="arch">
      <svg width="64" height="64" viewBox="0 0 64 64" fill="none" stroke="#1a84e0" stroke-width="3.5" stroke-linecap="round" stroke-linejoin="round"><path d="M36 10l18 18-10 10-18-18z"/><path d="M30 24 12 50l-4 6 6-2 26-20"/><path d="M44 16l-6 6M50 22l-6 6"/></svg>
    </div>
    <div class="box"><h3>Master keys<br>systems</h3><a class="more" href="#">Learn More ›</a></div>
  </div>
  <div class="service s4">
    <div class="arch">
      <svg width="66" height="66" viewBox="0 0 66 66" fill="none" stroke="#1a84e0" stroke-width="3" stroke-linejoin="round"><path d="M8 58V26l16-10v42M24 58V14L40 6v52M40 58V22h18v36M4 58h58"/><path d="M13 32h6M13 40h6M13 48h6M29 22h6M29 30h6M29 38h6M29 46h6M45 30h8M45 38h8M45 46h8"/></svg>
    </div>
    <div class="box"><h3>Commecial<br>service</h3><a class="more" href="#">Learn More ›</a></div>
  </div>
</section>

<section class="why">
  <svg class="notch" width="80" height="44" viewBox="0 0 80 44"><path d="M0 0h80L40 40z" fill="#fff"/><path d="M10 8 40 38 70 8" fill="none" stroke="#fff" stroke-width="3"/></svg>
  <h2>Why Choose Us</h2>
  <div class="copy">
    <p>consectetuer augue nisi quis lacus Ut ac mi quis lacus mollis aliquam Curabitur iaculis tempus eros Curabitur vel mi sit amet magna malesuada ultrices Ut nisi erat fermentum vel congue id euismod in elit</p>
    <p>Fusce ultricies orci ac feugiat suscipit leo massa sodales velit et scelerisque mi tortor at ipsum Proin orci odio commodo ac gravida non tristique vel tellus Pellentesque nibh libero ultricies eu sagittis non mollis sed justo Praesent metus ipsum pulvinar pulvinar porta id fringilla at est</p>
  </div>
  <a class="btn-outline" href="#">READ MORE</a>
</section>

<h2 class="cases-title">Recent Cases</h2>
<div class="case c1"><div class="photo" role="img" aria-label="Photo of a chrome car door handle and lock"></div><div class="label">Your Tittle here</div></div>
<div class="case c2"><div class="photo" role="img" aria-label="Photo of a gloved hand working on a car door lock"></div><div class="label">Your Tittle here</div></div>
<div class="case c3"><div class="photo" role="img" aria-label="Photo of hands picking a silver car door lock"></div><div class="label">Your Tittle here</div></div>
<div class="case c4"><div class="photo" role="img" aria-label="Photo of hands opening the lock on a red car door"></div><div class="label">Your Tittle here</div></div>

<section class="location">
  <div class="eyebrow">Where We Are</div>
  <h2>Our Location</h2>
  <p>Curabitur iaculis tempus eros Curabitur vel mi sit amet magna malesuada ultrices Ut nisi erat fermentum vel congue id euismod in elit Fusce ultricies orci ac feugiat suscipit leo</p>
  <div class="map" role="img" aria-label="Street map of central Melbourne marking the shop near the Corbett Row railway station"></div>
</section>

<footer class="site-footer">
  <div class="contact-item ci-addr">
    <svg width="14" height="20" viewBox="0 0 14 20"><path fill="#fff" d="M7 0C3.1 0 0 3.1 0 7c0 5 7 13 7 13s7-8 7-13c0-3.9-3.1-7-7-7zm0 9.5A2.5 2.5 0 1 1 7 4.5a2.5 2.5 0 0 1 0 5z"/></svg>
    <span>48 Corbett Row, Melbourne VIC 3000</span>
  </div>
  <div class="contact-item ci-phone">
    <svg width="19" height="19" viewBox="0 0 24 24" fill="none" stroke="#fff" stroke-width="1.8"><path d="M6.6 10.8c1.4 2.8 3.8 5.1 6.6 6.6l2.2-2.2c.3-.3.7-.4 1-.2 1.1.4 2.3.6 3.6.6.6 0 1 .4 1 1V20c0 .6-.4 1-1 1C10.6 21 3 13.4 3 4c0-.6.4-1 1-1h3.5c.6 0 1 .4 1 1 0 1.3.2 2.5.6 3.6.1.3 0 .7-.2 1L6.6 10.8z"/></svg>
    <span>03.9412.7731</span>
  </div>
  <div class="contact-item ci-mail">
    <svg width="20" height="15" viewBox="0 0 20 15" fill="none" stroke="#fff" stroke-width="1.6"><rect x="1" y="1" width="18" height="13" rx="1.5"/><path d="M1.5 2 10 8.5 18.5 2"/></svg>
    <span>hello@corbettrowlocks.com</span>
  </div>
  <nav class="footer-nav">
    <a href="#">Home</a><a href="#">About Us</a><a href="#">Services</a><a href="#">Cases</a><a href="#">Review</a><a href="#">Contact</a>
  </nav>
  <div class="copyright">© 2017 Company Name &nbsp;All right reserved &nbsp;Term of Use</div>
  <div class="social" aria-label="Social links"><span></span><span></span><span></span><span></span></div>
</footer>

</body>
</html>
```